Bright Sprouts Business Card

speech therapy business card that is fun and professional using my logo.
Updates

Wow wonderful dedigns ... 

Industry/Entity Type

Business

Contact Information for Business Card

Tessa Morvan
Brelow Certified Practising Speech Pathologist
B.Sp.Path MSPAA CPSP
ph: 0413906281
brightsproutsspeechpathology@mailbox.example
www.brightsproutsspeechpathology.example

```html
<!DOCTYPE html>
<html lang="en">
<head>
<meta charset="utf-8">
<title>Bright Sprouts Speech Pathology – Business Card</title>
<link rel="stylesheet" href="https://fonts.googleapis.com/css2?family=Noto+Serif:wght@400;700&display=swap">
<style>
  :root {
    --page: #ecebe8;
    --card: #ffffff;
    --ink: #3a3a3a;
    --ink-soft: #6d6d6d;
    --brand: #2f8fcf;
    --blue: #1f82c6;
    --yellow: #fcc81b;
    --green: #6cc24a;
    --plum: #5e1d5c;
    --lavender: #a77fa8;
    --gold-line: #f7cf3c;
  }
  * { box-sizing: border-box; margin: 0; padding: 0; }
  html, body { width: 1200px; height: 1000px; overflow: hidden; }
  body {
    background: var(--page);
    font-family: "Noto Serif", Georgia, serif;
    position: relative;
  }
  .business-card {
    position: absolute;
    left: 100px; top: 210px;
    width: 1000px; height: 580px;
    background: var(--card);
    overflow: hidden;
    box-shadow: 0 10px 30px rgba(0,0,0,.15);
  }
  .circle { position: absolute; border-radius: 50%; }
  .circle-email { width: 580px; height: 580px; left: 500px; top: -250px; background: var(--blue); }
  .circle-accent { width: 170px; height: 160px; left: 472px; top: 252px; background: var(--yellow); }
  .circle-phone { width: 270px; height: 270px; left: 610px; top: 235px; background: var(--green); z-index: 2; }

  .email-icon { position: absolute; left: 695px; top: 30px; width: 150px; height: 100px; }
  .email-text {
    position: absolute; left: 540px; top: 193px; width: 470px;
    text-align: center; color: #fff; font-size: 17px; letter-spacing: .3px;
  }
  .phone-icon { position: absolute; left: 718px; top: 268px; width: 62px; height: 90px; z-index: 3; }
  .phone-text {
    position: absolute; left: 610px; top: 378px; width: 270px; text-align: center;
    color: #fff; font-size: 30px; letter-spacing: 1.5px; z-index: 3;
  }

  .brand { position: absolute; left: 60px; top: 70px; display: flex; align-items: center; gap: 16px; }
  .brand-dot { width: 58px; height: 58px; border-radius: 50%; background: var(--green); flex: none; }
  .brand-name { color: var(--brand); font-size: 36px; font-weight: 700; line-height: 1.15; }

  .person { position: absolute; left: 60px; top: 268px; }
  .person-name { font-size: 34px; font-weight: 700; color: var(--ink-soft); letter-spacing: .5px; }
  .person-name span { color: var(--ink); }
  .person-role, .person-creds { font-size: 18px; color: var(--ink-soft); line-height: 1.35; }

  .footer-band {
    position: absolute; left: 0; bottom: 0; width: 100%; height: 120px;
    background: var(--lavender); border-top: 7px solid var(--gold-line);
  }
  .footer-band::before {
    content: ""; position: absolute; left: 0; top: 0; width: 720px; height: 62px;
    background: var(--plum);
    clip-path: polygon(0 0, 100% 0, 100% 100%, 0 100%);
  }
  .website {
    position: absolute; left: 60px; top: 24px; color: #fff;
    font-size: 24px; letter-spacing: 1px; z-index: 1;
  }
</style>
</head>
<body>
  <article class="business-card">
    <div class="circle circle-email"></div>
    <div class="circle circle-accent"></div>
    <div class="circle circle-phone"></div>

    <svg class="email-icon" viewBox="0 0 150 100" aria-hidden="true">
      <rect x="5" y="5" width="140" height="90" fill="none" stroke="#fff" stroke-width="8"/>
      <polyline points="5,5 75,58 145,5" fill="none" stroke="#fff" stroke-width="8"/>
      <line x1="5" y1="95" x2="58" y2="46" stroke="#fff" stroke-width="6"/>
      <line x1="145" y1="95" x2="92" y2="46" stroke="#fff" stroke-width="6"/>
    </svg>
    <p class="email-text">brightsproutsspeechpathology@mailbox.example</p>

    <svg class="phone-icon" viewBox="0 0 62 90" aria-hidden="true">
      <path fill="#fff" d="M14 4c5-3 9-2 11 3l6 14c1 4 0 7-4 9l-5 3c-2 1-2 3-1 6 3 9 7 17 13 24 2 2 4 2 6 1l5-3c4-2 7-2 9 1l7 12c2 4 1 8-3 10l-6 4c-6 3-13 2-18-3C19 69 9 48 6 28 5 18 7 9 14 4z"/>
    </svg>
    <p class="phone-text">0413906281</p>

    <header class="brand">
      <div class="brand-dot"></div>
      <div class="brand-name">Bright Sprouts<br>Speech Pathology</div>
    </header>

    <section class="person">
      <h1 class="person-name"><span>Tessa Morvan</span> Brelow</h1>
      <p class="person-role">Certified Practising Speech Pathologist</p>
      <p class="person-creds">B.S.P. Path MSPAA CPSP</p>
    </section>

    <footer class="footer-band">
      <p class="website">www.brightsproutsspeechpathology.example</p>
    </footer>
  </article>
</body>
</html>
```